Grivo like IOS/Android app for Okinawa Island - TavuScout

TavuScout is the name of the app
The closest thing that I can relate this app to is a region specific Grivo app. The app is for the island of Okinawa and is geared towards English speaking travelers. The style of app that I prefer is a look and feel similar to that of the new Lodgemere app, color should also be similar if not the same as the lodgemere app.

The app needs to have the following screens

LOGIN SCREEN
1. App login page with a login for chatterly button or create an account option. Personally I would like an image in the background with a real beachy feel, but don't do this if it messes with your design.

2. Depending on the choice of login there will need to be a second login screen to create the account. Lodgemere does this nicely.

PRIMARY HOME
primary page similar to the primary layout when you get into the lodgemere app.
This page is kind of like the home page of the app and should include the following items:
search field
upcoming events
popular things to do
featured restaurants
Featured Places to stay
area guides
Moving here
(this will allow the person to select, housing agencies, auto dealers, schools etc) These are essentially just quick searches.
Each selection should be listed so that the user can swipe to the left or right in order to view more listings under the categories listed above. It will not be the full list but rather a sample.

SIDEBAR POPOUT MENU
Popout sidebar that contains the following selections
Places to Eat
Things to do
Attractions
Beaches
Shop
Farmers Markets
Places to Stay
Schools & DayCare
Housing
Auto
Events
Account settings
Add a business

LIST VIEW
4. List view page for whatever category the user selected. This will show all the listings for the specific category: The top should also have the featured listings for that category

INDIVIDUAL LISTING
5. Listing page
This will include photos, description, hours, map(this can be a button to view the map or the map), Reviews with a leave a review option

AREA GUIDES
6. Area Guides. This is where the user will be able to select a specific area and learn about it. It should include an area where there can be a description, photos with a hero photo image, a map, popular local attractions or things to do, best restaurants in the area, places to stay etc.

PROFILE PAGE
7. Profile page for the user where they can make any updates they need to

Every page but the listing page should include the search bar. When the user clicks in it they should be able to see a drop down of quick select searches or run a regular search.

Logo
I have attached a logo that was made that needs a redesign. The map marker contains the logo for Okinawa within it so it does need to be similar.

If you have any questions or need clarification please send me a message. I will respond promptly.
Thank you,

```html
<!DOCTYPE html>
<html lang="en">
<head>
<meta charset="utf-8">
<title>TavuScout – Welcome</title>
<link rel="stylesheet" href="https://fonts.googleapis.com/css2?family=Jost:wght@400;500&display=swap">
<style>
  :root {
    --canvas-bg: #e9e7e4;
    --screen-bg: #ffffff;
    --brand: #e8576a;
    --brand-pink: #e85b8c;
    --social-blue: #3d5a9a;
    --muted: #9b9b9b;
    --status-text: #e8576a;
    --button-text: #ffffff;
  }
  * { box-sizing: border-box; margin: 0; padding: 0; }
  html, body {
    width: 1106px;
    height: 1200px;
    overflow: hidden;
    background: var(--canvas-bg);
    font-family: "Jost", "Futura", sans-serif;
  }
  .canvas {
    width: 1106px;
    height: 1200px;
    display: flex;
    justify-content: center;
  }
  .screen {
    position: relative;
    width: 676px;
    height: 1200px;
    background: var(--screen-bg);
  }
  .status-bar {
    position: absolute;
    top: 0; left: 0; right: 0;
    height: 42px;
    display: flex;
    align-items: center;
    justify-content: space-between;
    padding: 0 14px;
    color: var(--status-text);
    font-size: 17px;
  }
  .status-bar .carrier { display: flex; align-items: center; gap: 6px; }
  .status-bar .signal { letter-spacing: -2px; font-size: 12px; }
  .status-bar .time { position: absolute; left: 50%; transform: translateX(-50%); }
  .status-bar .battery { display: flex; align-items: center; gap: 6px; }
  .battery-icon {
    width: 34px; height: 15px;
    border: 1.5px solid var(--status-text);
    border-radius: 3px;
    padding: 1.5px;
  }
  .battery-icon span { display: block; width: 80%; height: 100%; background: var(--status-text); border-radius: 1px; }

  .brand-mark {
    position: absolute;
    top: 236px;
    left: 50%;
    transform: translateX(-50%);
    width: 72px; height: 72px;
    border-radius: 50%;
    background: var(--brand);
  }
  .welcome-title {
    position: absolute;
    top: 362px;
    width: 100%;
    text-align: center;
    color: var(--brand);
    font-size: 38px;
    font-weight: 500;
    letter-spacing: 0.5px;
  }
  .welcome-tagline {
    position: absolute;
    top: 424px;
    width: 100%;
    text-align: center;
    color: var(--muted);
    font-size: 21px;
    font-weight: 400;
  }
  .auth-actions {
    position: absolute;
    top: 672px;
    left: 50%;
    transform: translateX(-50%);
    width: 440px;
    display: flex;
    flex-direction: column;
    gap: 28px;
    align-items: center;
  }
  .btn {
    width: 100%;
    height: 76px;
    border-radius: 38px;
    display: flex;
    align-items: center;
    justify-content: center;
    color: var(--button-text);
    font-size: 25px;
    font-weight: 400;
    text-transform: uppercase;
    letter-spacing: 0.3px;
  }
  .btn-social { background: var(--social-blue); }
  .btn-signup { background: linear-gradient(90deg, var(--brand-pink), var(--brand)); }
  .member-prompt {
    margin-top: -6px;
    color: var(--muted);
    font-size: 23px;
  }
  .member-prompt .login-link { color: var(--brand); text-transform: uppercase; }
</style>
</head>
<body>
  <main class="canvas">
    <section class="screen">
      <header class="status-bar">
        <div class="carrier"><span class="signal">●●●○○</span><span>Strokei</span></div>
        <div class="time">1:43 pm</div>
        <div class="battery"><span>80%</span><div class="battery-icon"><span></span></div></div>
      </header>

      <div class="brand-mark" aria-hidden="true"></div>
      <h1 class="welcome-title">Welcome to TavuScout</h1>
      <p class="welcome-tagline">For travelers of Okinawa</p>

      <div class="auth-actions">
        <div class="btn btn-social">Login with chatterly</div>
        <div class="btn btn-signup">Sign up</div>
        <p class="member-prompt">Already a member? <span class="login-link">Login</span></p>
      </div>
    </section>
  </main>
</body>
</html>
```